Business Card Design Project

Hi. We need a new business card for Brightfield Partners, a consultancy that helps people with online marketing strategy and solutions.

We have a new logo and now need the info presented - front and back of business card.

FRONT

Logo

Online strategy, consulting and coaching
Varlo Admarket consulting
Search Engine Optimisation
Internet Lead Generation
Domain name broking

BACK

Tom Bradwell-Jones
+ 61 83215 9076
+ 61 (0) 418 536 207
tom@brightfieldpartners.com.au
www.brightfieldpartners.com.au

Talkora: tombradwelljones
PO Box 312, Marlow Heights, Westland 6072

Target Market(s)

Business owners, corporates

Industry/Entity Type

Marketing

Requirements
Must have
• double sided
size: 86 x 54mm
supplied as one pdf with crop marks shown (+- 1mm, with 2-3 mm bleed)

```html
<!DOCTYPE html>
<html lang="en">
<head>
<meta charset="utf-8">
<title>Brightfield Partners Business Card</title>
<link rel="stylesheet" href="https://fonts.googleapis.com/css2?family=Exo+2:wght@400;500;700&display=swap">
<style>
  :root {
    --backdrop-top: #8c8c8c;
    --backdrop-bottom: #b9b9b9;
    --card-white: #ffffff;
    --card-white-shade: #eef0f2;
    --accent-orange: #f0922b;
    --accent-orange-light: #f7a442;
    --brand-blue: #2c5289;
    --navy-dark: #1c3a66;
    --navy-light: #34609a;
    --text-light: #ffffff;
  }
  * { box-sizing: border-box; margin: 0; padding: 0; }
  html, body { width: 1200px; height: 861px; overflow: hidden; }
  body {
    font-family: "Exo 2", sans-serif;
    background: linear-gradient(180deg, var(--backdrop-top), var(--backdrop-bottom));
    position: relative;
  }
  .card-set {
    position: absolute;
    left: 70px; top: 273px;
    display: flex; gap: 60px;
  }
  .card {
    position: relative;
    width: 500px; height: 314px;
    border-radius: 14px;
    overflow: hidden;
    background: linear-gradient(160deg, var(--navy-light), var(--navy-dark));
    box-shadow: 0 10px 24px rgba(0,0,0,0.25);
  }
  .card__top {
    position: absolute; left: 0; top: 0; right: 0; height: 132px;
    background: linear-gradient(180deg, var(--card-white), var(--card-white-shade));
  }
  .card__band {
    position: absolute; left: 0; right: 0; top: 132px; height: 18px;
    background: var(--accent-orange);
  }
  .card__tab {
    position: absolute; top: 132px; height: 46px;
    background: linear-gradient(180deg, var(--accent-orange), var(--accent-orange-light));
    border-radius: 0 0 16px 16px;
    color: var(--text-light);
    display: flex; align-items: center; justify-content: center;
    padding-top: 4px;
    white-space: nowrap;
  }
  .card--front .card__tab { left: 164px; width: 304px; font-size: 16px; }
  .card--back .card__tab { left: 40px; width: 262px; font-size: 23px; font-weight: 500; letter-spacing: 0.3px; }

  .brand-mark {
    position: absolute; top: 50px;
    display: flex; align-items: center; gap: 10px;
  }
  .card--front .brand-mark { right: 52px; }
  .card--back .brand-mark { left: 50px; }
  .brand-mark__dot {
    width: 34px; height: 34px; border-radius: 50%;
    background: var(--accent-orange);
  }
  .brand-mark__name {
    font-size: 25px; font-weight: 700; color: var(--brand-blue);
    letter-spacing: 0.2px;
  }

  .service-list {
    position: absolute; left: 62px; top: 196px;
    list-style: none; color: var(--text-light);
    font-size: 15px; line-height: 21px;
  }
  .service-list li::before {
    content: ">"; font-weight: 700; margin-right: 7px; font-size: 13px;
  }

  .contact-list {
    position: absolute; left: 272px; top: 180px;
    list-style: none; color: var(--text-light);
    font-size: 12px; line-height: 16px;
  }
  .contact-list li { display: flex; align-items: flex-start; gap: 7px; white-space: nowrap; }
  .contact-list svg { width: 11px; height: 11px; margin-top: 2px; flex: none; fill: var(--text-light); }
</style>
</head>
<body>
  <main class="card-set">
    <section class="card card--front" aria-label="Card front">
      <div class="card__top"></div>
      <div class="card__band"></div>
      <div class="brand-mark">
        <span class="brand-mark__dot"></span>
        <span class="brand-mark__name">Brightfield Partners</span>
      </div>
      <div class="card__tab">www.brightfieldpartners.com.au</div>
      <ul class="service-list">
        <li>Online strategy, consulting and coaching</li>
        <li>Varlo Admarket consulting</li>
        <li>Search Engine Optimisation</li>
        <li>Internet Lead Generation</li>
        <li>Domain name broking</li>
      </ul>
    </section>

    <section class="card card--back" aria-label="Card back">
      <div class="card__top"></div>
      <div class="card__band"></div>
      <div class="brand-mark">
        <span class="brand-mark__dot"></span>
        <span class="brand-mark__name">Brightfield Partners</span>
      </div>
      <div class="card__tab">Tom Bradwell-Jones</div>
      <ul class="contact-list">
        <li>
          <svg viewBox="0 0 12 12" aria-hidden="true"><path d="M1 11V2h6v9zM8 11V5h3v6zM2.5 3.5h1v1h-1zM4.5 3.5h1v1h-1zM2.5 6h1v1h-1zM4.5 6h1v1h-1z" fill-rule="evenodd"/></svg>
          <span>PO Box 312, Marlow Heights,<br>Westland 6072</span>
        </li>
        <li>
          <svg viewBox="0 0 12 12" aria-hidden="true"><path d="M2 1l2.5 0 1 3-1.5 1c.7 1.4 1.6 2.3 3 3l1-1.5 3 1V11c-5 0-9-4-9-9z"/></svg>
          <span>+ 61 83215 9076</span>
        </li>
        <li>
          <svg viewBox="0 0 12 12" aria-hidden="true"><path d="M3.5 0.5h5v11h-5zM4.5 2v6.5h3V2z" fill-rule="evenodd"/></svg>
          <span>+ 61 (0) 418 536 207</span>
        </li>
        <li>
          <svg viewBox="0 0 12 12" aria-hidden="true"><circle cx="6" cy="6" r="5.5"/></svg>
          <span>tombradwelljones</span>
        </li>
        <li>
          <svg viewBox="0 0 12 12" aria-hidden="true"><path d="M0.5 2.5h11v7h-11zM1.5 3.5l4.5 3.2 4.5-3.2v.9L6 7.7 1.5 4.4z" fill-rule="evenodd"/></svg>
          <span>tom@brightfieldpartners.com.au</span>
        </li>
        <li>
          <svg viewBox="0 0 12 12" aria-hidden="true"><path d="M0.5 1.5h11v7.5h-11zM1.5 2.5v5.5h9V2.5zM4 10h4v1H4z" fill-rule="evenodd"/></svg>
          <span>www.brightfieldpartners.com.au</span>
        </li>
      </ul>
    </section>
  </main>
</body>
</html>
```